Business Card design for Recruiter providing Recruitment Staff Augmentation services

I need a double sided business card. I have used Zek to print cards in the past and really like their quality. I have a logo but need to change the tagline that is part of the graphic.

The tagline currently reads and Connnecting people with careers - but it should be removed.

The back should look like a notecard for writing a to do list with the first to-do Augment Recruiting Staff

```html
<!DOCTYPE html>
<html lang="en">
<head>
<meta charset="utf-8">
<title>Talent Forge – Business Card</title>
<link rel="stylesheet" href="https://fonts.googleapis.com/css2?family=Questrial&family=Arimo:wght@400&display=swap">
<style>
  :root {
    --page: #e9e7e3;
    --card: #fbfbfb;
    --navy: #0f4a70;
    --orange: #d8562b;
    --ghost-ring: rgba(216, 86, 43, 0.10);
    --ghost-fill: rgba(15, 74, 112, 0.04);
    --rule: #e08a66;
  }
  * { box-sizing: border-box; margin: 0; padding: 0; }
  html, body { width: 1200px; height: 1023px; overflow: hidden; }
  body {
    background: var(--page);
    position: relative;
    font-family: "Arimo", Arial, sans-serif;
  }
  .card {
    position: absolute;
    width: 540px;
    height: 315px;
    background: var(--card);
    border-radius: 16px;
    overflow: hidden;
    box-shadow: 0 6px 18px rgba(0,0,0,0.18);
  }
  .card--front { left: 330px; top: 90px; }
  .card--back  { left: 330px; top: 560px; }

  .band {
    position: absolute; left: 0; top: 0; bottom: 0; width: 60px;
    background: var(--navy);
  }
  .ghost-mark {
    position: absolute; border-radius: 50%;
    border: 3px solid var(--ghost-ring);
    background: var(--ghost-fill);
  }
  .card--front .ghost-mark { width: 170px; height: 170px; right: 24px; top: 112px; }
  .card--back .ghost-mark  { width: 190px; height: 190px; left: 70px; top: 90px; }

  .brand { position: absolute; display: flex; align-items: center; gap: 12px; }
  .brand__dot {
    width: 46px; height: 46px; border-radius: 50%;
    border: 3px solid var(--orange);
  }
  .brand__name {
    font-family: "Questrial", sans-serif;
    color: var(--navy);
    font-size: 40px; line-height: 1; letter-spacing: 1px;
  }
  .card--front .brand { left: 76px; top: 28px; }
  .card--back .brand { right: 26px; top: 36px; }
  .card--back .brand__name { font-size: 34px; }
  .card--back .brand__dot { width: 40px; height: 40px; }

  .person { position: absolute; left: 80px; top: 108px; }
  .person__name { color: var(--orange); font-size: 24px; letter-spacing: 0.5px; line-height: 1.2; }
  .person__title { color: var(--navy); font-size: 14px; margin-top: 2px; }

  .contact-icons {
    position: absolute; left: 16px; top: 178px;
    display: flex; flex-direction: column; gap: 8px;
  }
  .contact-icons svg { width: 26px; height: 26px; display: block; }
  .contacts {
    position: absolute; left: 80px; top: 178px;
    list-style: none; color: var(--orange);
    font-size: 14px; letter-spacing: 1px;
  }
  .contacts li { height: 34px; line-height: 26px; }

  .note-lines { position: absolute; left: 30px; right: 30px; top: 130px; }
  .note-lines hr {
    border: none; border-top: 1px solid var(--rule);
    margin-bottom: 52px;
  }
</style>
</head>
<body>

<section class="card card--front" aria-label="Business card front">
  <div class="band"></div>
  <div class="ghost-mark"></div>

  <div class="brand">
    <span class="brand__dot"></span>
    <span class="brand__name">TALENT FORGE</span>
  </div>

  <div class="person">
    <div class="person__name">Dana Whitlock, SPHR</div>
    <div class="person__title">Title</div>
  </div>

  <div class="contact-icons">
    <svg viewBox="0 0 26 26" aria-label="Phone">
      <circle cx="13" cy="13" r="11.5" fill="none" stroke="#fff" stroke-width="2"/>
      <path d="M9 7.5c-1 1-1 3 1 6s4.5 5 6 4.5l1.5-1.5-2.5-2-1.3 1c-1-.5-2.5-2-3-3l1-1.3-2-2.5z" fill="#fff"/>
    </svg>
    <svg viewBox="0 0 26 26" aria-label="Office">
      <circle cx="13" cy="13" r="11.5" fill="none" stroke="#fff" stroke-width="2"/>
      <rect x="7.5" y="8" width="11" height="10" rx="1.5" fill="none" stroke="#fff" stroke-width="1.6"/>
    </svg>
    <svg viewBox="0 0 26 26" aria-label="Email">
      <circle cx="13" cy="13" r="11.5" fill="none" stroke="#fff" stroke-width="2"/>
      <rect x="7" y="9" width="12" height="8" fill="none" stroke="#fff" stroke-width="1.5"/>
      <path d="M7 9l6 5 6-5" fill="none" stroke="#fff" stroke-width="1.5"/>
    </svg>
    <svg viewBox="0 0 26 26" aria-label="Website">
      <circle cx="13" cy="13" r="11.5" fill="none" stroke="#fff" stroke-width="2"/>
      <circle cx="13" cy="13" r="6" fill="none" stroke="#fff" stroke-width="1.4"/>
      <path d="M7 13h12M13 7c-3 3-3 9 0 12M13 7c3 3 3 9 0 12" fill="none" stroke="#fff" stroke-width="1.2"/>
    </svg>
  </div>

  <ul class="contacts">
    <li>555-014-2280</li>
    <li>555-014-2280</li>
    <li>Dana@talentforge.example</li>
    <li>www.talentforge.example</li>
  </ul>
</section>

<section class="card card--back" aria-label="Business card back">
  <div class="ghost-mark"></div>
  <div class="brand">
    <span class="brand__dot"></span>
    <span class="brand__name">TALENT FORGE</span>
  </div>
  <div class="note-lines">
    <hr><hr><hr>
  </div>
</section>

</body>
</html>
```